Letter Head Design - Finance industry

Design a letterhead to match the logo. Needs to be clean, simple and crisp. I'm open to suggestions. Will be using the logo that was submitted last with the W crossed over

Target Market(s)

Small medium businesses and government department's

Industry/Entity Type

Industry

Font styles to use
Sans Serif

Colors
cadf82
bcd85c
acd036
9bcb3c
e9e9e9
aaaaaa
000000
7f7f7f
b7b7b7

Requirements
Must have
• Need to display: Logo, Business address, ABN number, ASIC register number, contact phone, website, company email. Details are as per below:

Suite 4B Level 17
Marlowe Harbour Tower
9 Tindall Place
Sydney NSW 2000
Landline Ph: 02 5193 2604
Ph: 1300 4917 63
Email: enquiries@brightmoorfin.com.au
W: www.brightmoorfin.com.au

On the footer, the details below need to be specified:
ABN: 43 719 385 207
ASIC Registration Number: 27 318640571

Should not have
• No imagery or design that is not in line with the logo

```html
<!DOCTYPE html>
<html lang="en">
<head>
<meta charset="utf-8">
<title>Brightmoor Finance — Letterhead</title>
<link rel="stylesheet" href="https://fonts.googleapis.com/css2?family=EB+Garamond:wght@400;600&family=Merriweather:ital,wght@1,900&family=Quattrocento+Sans:wght@400&display=swap">
<style>
  :root {
    --backdrop: #2a2a2a;
    --paper: #ffffff;
    --green: #9bcb3c;
    --green-band: #9bcb3c;
    --ink: #000000;
    --grey: #7f7f7f;
    --rule: #aaaaaa;
  }
  * { margin: 0; padding: 0; box-sizing: border-box; }
  html, body {
    width: 1000px; height: 1200px; overflow: hidden;
    background: var(--backdrop);
  }
  .letterhead {
    position: absolute; left: 155px; top: 82px;
    width: 717px; height: 1013px;
    background: var(--paper);
  }
  .brand {
    position: absolute; left: 0; right: 0; top: 80px;
    text-align: center;
    font-family: "EB Garamond", serif;
    font-size: 19px; font-weight: 600;
    color: var(--green);
  }
  .address {
    position: absolute; left: 0; right: 0; top: 119px;
    text-align: center;
    font-family: "EB Garamond", serif;
    font-size: 11.5px; color: var(--grey);
  }
  .rule { position: absolute; height: 1px; width: 74px; background: var(--rule); }
  .rule--tl { left: 0; top: 126px; }
  .rule--tr { right: 0; top: 126px; }
  .rule--bl { left: 0; top: 901px; }
  .rule--br { right: 0; top: 901px; }

  .letter {
    position: absolute; left: 116px; top: 314px; width: 486px;
    font-family: "Quattrocento Sans", sans-serif;
    font-size: 10.6px; line-height: 14.4px; color: var(--ink);
  }
  .salutation, .closing {
    font-family: "Merriweather", serif;
    font-style: italic; font-weight: 900;
    font-size: 12px; line-height: 16px;
  }
  .salutation { margin-bottom: 18px; }
  .letter p.body { text-align: justify; hyphens: auto; margin-bottom: 15px; }
  .closing { margin-top: -1px; }
  .signoff {
    font-family: "EB Garamond", serif; font-size: 11px;
    color: var(--grey); margin-left: 2px; line-height: 14px;
  }

  .contact {
    position: absolute; top: 930px; left: 116px;
    font-family: "EB Garamond", serif; font-size: 10.5px;
    line-height: 17px; color: var(--grey);
  }
  .contact .label { color: var(--green); font-weight: 600; }
  .contact--web { left: 116px; }
  .contact--phone { left: 306px; }
  .contact--phone .indent { display: block; text-align: right; }
  .contact--reg { left: 440px; }
  .band {
    position: absolute; left: 0; right: 0; bottom: 0; height: 15px;
    background: var(--green-band);
  }
</style>
</head>
<body>
  <main class="letterhead">
    <div class="brand">Brightmoor Finance</div>
    <div class="address">Suite 4B Level 17, Marlowe Harbour Tower, 9 Tindall Place, Sydney NSW 2000</div>
    <span class="rule rule--tl"></span><span class="rule rule--tr"></span>

    <article class="letter" lang="en">
      <p class="salutation">Dear MR. John,</p>
      <p class="body">Lorem ipsum dolor sit amet, consectetur adipiscing elit. In posuere ornare magna, vitae porttitor diam mollis eu. Aenean molestie at turpis a tristique. Sed ac ultricies magna. Proin vehicula eros eu enim rhoncus, ut ultrices purus adipiscing. Quisque vehicula ligula at sem luctus dapibus. In iaculis neque eget nulla condimentum ornare. Aliquam non sem facilisis dui ornare aliquam. Maecenas adipiscing mauris sit amet fermentum vehicula. Aliquam eleifend et enim ac tincidunt. Vestibulum pharetra malesuada sagittis.</p>
      <p class="body">Integer nibh purus, pharetra egestas cursus vel, mattis nec quam. Vestibulum quis placerat est, ut aliquet tellus. Quisque auctor neque quam, ac rhoncus mauris convallis nec. Suspendisse ullamcorper ligula a nunc pellentesque scelerisque dignissim ut metus. Vivamus felis mi, sollicitudin id ultrices in, tristique vitae quam. Ut bibendum interdum erat, nec aliquet enim mattis dignissim. Aenean augue purus, aliquet ac sollicitudin sed, commodo in libero. Phasellus sagittis enim in dui commodo mollis. Fusce vitae tempor leo, ut ultrices justo. Nullam tellus elit, laoreet et posuere sit amet, viverra ut tellus. Donec sagittis sapien sed odio elementum congue. Nam egestas, enim nec molestie ullamcorper, mauris neque tempus est, a aliquam eros ante id sem. Duis risus orci, condimentum vitae magna ac, pellentesque tincidunt velit.</p>
      <p class="body">Curabitur venenatis, enim nec tincidunt semper, leo lectus rhoncus lacus, ac tristique felis tortor et lorem. Nunc sollicitudin mauris in justo hendrerit consectetur. Sed sed semper sapien, sit amet bibendum diam. Quisque tempus nisl velit, sed egestas sapien tempus ut. Morbi vel vehicula arcu, ut pharetra nunc. Quisque vel commodo nunc, et euismod metus. Nulla ligula sapien, fringilla eu placerat posuere, tempor quis justo. In pharetra vehicula dui, sed tristique mauris semper a. Nullam laoreet viverra elit, vel porttitor dolor laoreet ut. Integer volutpat orci elit, non rhoncus felis pretium non. Curabitur eu porta arcu.</p>
      <p class="closing">Your Sincerely,</p>
      <p class="signoff">BF.</p>
    </article>

    <span class="rule rule--bl"></span><span class="rule rule--br"></span>

    <footer>
      <div class="contact contact--web">
        <span class="label">Email:</span> enquiries@brightmoorfin.com.au<br>
        <span class="label">Web:</span> www.brightmoorfin.com.au
      </div>
      <div class="contact contact--phone">
        <span class="label">Landline</span> Ph: 02 5193 2604
        <span class="indent">Ph: 1300 4917 63</span>
      </div>
      <div class="contact contact--reg">
        <span class="label">ABN:</span> 43 719 385 207<br>
        <span class="label">ASIC:</span> Registration Number: XXXXXX
      </div>
    </footer>
    <div class="band"></div>
  </main>
</body>
</html>
```